A flyer for future customers to get acquainted with our company

The flyer/card is intended for intermediaries. The purpose of this flyer is to introduce businesses to Dovrel.

It should convey: real estate and financing, with actual images. Various keywords describing what we do: project financing, temporary real estate financing, real estate financing, investment properties, transformations. We distinguish ourselves by being fast, flexible, and personal.

Please ensure the front has an attractive and inviting appearance, and leave space on the back for additional text.

Color codes: #E85B35 en #091E33

```html
<!DOCTYPE html>
<html lang="en">
<head>
<meta charset="utf-8">
<title>Dovrel – Real Estate Financing</title>
<link href="https://fonts.googleapis.com/css2?family=Poppins:wght@500;700;800;900&display=swap" rel="stylesheet">
<style>
  :root {
    --orange: #E85B35;
    --navy: #091E33;
    --white: #ffffff;
    --paper: #f6f6f4;
  }
  * { margin: 0; padding: 0; box-sizing: border-box; }
  html, body { width: 1200px; height: 857px; overflow: hidden; background: var(--navy); }
  .flyer {
    position: relative;
    width: 1200px;
    height: 857px;
    overflow: hidden;
    font-family: "Poppins", sans-serif;
  }
  .backdrop-photo {
    position: absolute; inset: 0;
    background: linear-gradient(180deg, #7fb3ae 0%, #a9c6c4 22%, #5c7d86 42%, #27405a 62%, #0e2740 78%, var(--navy) 100%);
  }
  .presenter-photo {
    position: absolute;
    left: 690px; top: 148px;
    width: 450px; height: 600px;
    border-radius: 200px 200px 0 0;
    background: linear-gradient(180deg, #5a3a2c 0%, #c63a2a 35%, #b8322a 70%, #8f2520 100%);
  }
  .brand-tab {
    position: absolute;
    left: 100px; top: 0;
    width: 289px; height: 134px;
    background: var(--paper);
    border-bottom: 6px solid var(--orange);
    border-right: 6px solid var(--orange);
    border-bottom-right-radius: 48px;
    display: flex; align-items: center; justify-content: center;
  }
  .brand-name {
    font-weight: 700;
    font-size: 58px;
    color: var(--navy);
    letter-spacing: -1px;
  }
  .headline {
    position: absolute;
    left: 96px; top: 214px;
    font-weight: 800;
    line-height: 1;
  }
  .headline-lead {
    display: block;
    font-size: 108px;
    color: var(--white);
    -webkit-text-stroke: 4px var(--orange);
    paint-order: stroke fill;
    letter-spacing: -1px;
  }
  .headline-rest {
    display: block;
    font-size: 75px;
    color: var(--orange);
    line-height: 0.9;
    margin-top: 4px;
  }
  .money-bag { position: absolute; left: 514px; top: 432px; width: 96px; height: 116px; }
  .divider {
    position: absolute; left: 100px; top: 574px;
    width: 297px; height: 3px; background: var(--white);
  }
  .services {
    position: absolute; left: 98px; top: 593px;
    list-style: none;
  }
  .service {
    display: flex; align-items: center;
    height: 51px;
    color: var(--white);
    font-weight: 500;
    font-size: 24px;
    letter-spacing: 1.2px;
  }
  .service-icon {
    width: 38px; height: 38px; border-radius: 50%;
    background: var(--white);
    margin-right: 11px;
    display: flex; align-items: center; justify-content: center;
  }
  .service-icon svg { width: 24px; height: 24px; }
  .bottom-wave { position: absolute; left: 0; top: 0; width: 1200px; height: 857px; }
  .values {
    position: absolute; left: 949px; top: 736px;
    list-style: none;
  }
  .value {
    display: flex; align-items: center;
    height: 33.5px;
    color: var(--white);
    font-weight: 800;
    font-size: 27px;
    letter-spacing: 1px;
  }
  .value::before {
    content: "";
    width: 13px; height: 13px;
    background: var(--navy);
    margin-right: 17px;
  }
</style>
</head>
<body>
<main class="flyer">
  <div class="backdrop-photo" role="img" aria-label="Photo of a modern white two-storey villa with glass walls and wooden slats, trees and a hillside behind it"></div>
  <div class="presenter-photo" role="img" aria-label="Photo of a smiling businessman in a red blazer holding a small model of a red house"></div>

  <svg class="bottom-wave" viewBox="0 0 1200 857" aria-hidden="true">
    <path d="M0,803 C700,800 1020,730 1200,583 L1200,857 L0,857 Z" fill="var(--white)"/>
    <path d="M0,810 C700,807 1030,740 1200,596 L1200,857 L0,857 Z" fill="var(--orange)"/>
  </svg>

  <header class="brand-tab">
    <span class="brand-name">Dovrel</span>
  </header>

  <h1 class="headline">
    <span class="headline-lead">Unlocking</span>
    <span class="headline-rest">Possibilities in<br>Real Estate<br>Financing</span>
  </h1>

  <svg class="money-bag" viewBox="0 0 96 116" aria-hidden="true">
    <g transform="rotate(20 48 70)">
      <path d="M36,30 C28,16 40,10 48,18 C56,10 68,16 60,30 Z" fill="var(--orange)" stroke="var(--white)" stroke-width="4"/>
      <path d="M38,32 C10,50 6,102 48,104 C90,102 86,50 58,32 Z" fill="var(--orange)" stroke="var(--white)" stroke-width="4"/>
      <text x="48" y="82" text-anchor="middle" font-family="Poppins, sans-serif" font-weight="800" font-size="30" fill="var(--white)">$</text>
    </g>
  </svg>

  <div class="divider"></div>

  <ul class="services">
    <li class="service">
      <span class="service-icon"><svg viewBox="0 0 24 24"><rect x="3" y="7" width="14" height="11" rx="2" fill="var(--orange)"/><rect x="7" y="4" width="6" height="4" rx="1" fill="none" stroke="var(--orange)" stroke-width="2"/><circle cx="18" cy="17" r="5" fill="var(--orange)" stroke="var(--white)" stroke-width="1.5"/></svg></span>
      Project Financing
    </li>
    <li class="service">
      <span class="service-icon"><svg viewBox="0 0 24 24"><rect x="5" y="6" width="15" height="14" rx="2" fill="var(--orange)"/><circle cx="7" cy="7" r="5" fill="var(--orange)" stroke="var(--white)" stroke-width="1.5"/><rect x="14" y="11" width="6" height="4" rx="1" fill="var(--white)"/></svg></span>
      Temporary Real Estate Financing
    </li>
    <li class="service">
      <span class="service-icon"><svg viewBox="0 0 24 24"><path d="M3,9 L12,3 L21,9 Z" fill="var(--orange)"/><rect x="4" y="10" width="16" height="9" fill="var(--orange)"/><rect x="3" y="19" width="18" height="2" fill="var(--orange)"/><rect x="9" y="12" width="6" height="5" fill="var(--white)"/></svg></span>
      Investiment Properties
    </li>
    <li class="service">
      <span class="service-icon"><svg viewBox="0 0 24 24"><circle cx="12" cy="12" r="9" fill="none" stroke="var(--orange)" stroke-width="3" stroke-dasharray="4 2"/><circle cx="12" cy="12" r="6" fill="var(--orange)"/><text x="12" y="16" text-anchor="middle" font-family="Poppins, sans-serif" font-weight="800" font-size="10" fill="var(--white)">$</text></svg></span>
      Transformations
    </li>
  </ul>

  <ul class="values">
    <li class="value">Fast</li>
    <li class="value">Flexible</li>
    <li class="value">Personal</li>
  </ul>
</main>
</body>
</html>
```